依頼詳細
パルミナで販売する電子書籍の表紙デザインを依頼します。

<ポイント>
・テキストは横書きでお願いします。斜体は使わないでください。
・サムネイルになってもタイトルが認識できるようにしてください。
・対象読者は主に20代~50代の女性です。

<追加していただくテキスト>
【タイトル】
ひだまり食卓ノート

【キャッチコピー】
グルテンフリー食生活で体をいたわり
真の健康を目指しましょう

【著者】
ロウェンタール・ミサキ
記載項目
パルミナのサイトには「長辺が最低1000ピクセル、理想的な縦横比は1.6、長辺が2500ピクセルの表紙画像が推奨」と記載されていますのでそれに合わせて最適なものを作ってください。

<写真素材>
自由に加工可能な3点の写真素材を用意しましたので、それを組み込んでいただきたいと思います。

(1) Gluten Free 3 Loaf of Bread.jpg (パン3斤の商品の写真)
(2) Gluten Free Bread Slice.jpg (パン1枚の写真)
(3) Gluten Free Symbol.jpg (グルテンフリーのシンボル)

上の写真の (1) または (2) のどちらか1つを、表紙全体の半分~3分の2程度の大きさに組み込み、残りの部分は無地にしてそこにタイトルやキャッチコピーを入れていただければと思い ます。無地の背景の色はおまかせします。写真の位置は、上でも中央でも下でもかまいません。著者名は小さめで目立たなくていいです。著者名の位置はおまか せします。
(1) のパン3斤の写真を使っていただく場合、この写真の背景がごちゃごちゃしているのでさらにぼかしていただくか、クロップしてください。
(3) のシンボルは使っても使わなくてもいいのですが、使う場合は縮小してアクセントとして使ってください。
希望イメージ
シンプル 複雑
単色 カラフル
暗い 明るい
日常 高級
遊び心 厳粛
未来的 伝統的
女性的 男性的
希望する色
画像に合う色を使ってください
納品ファイル
• 高解像度JPG (.jpg)
• イラストレーター形式 (.ai)
補足説明
■ 選んだ理由

タイトルがサムネイル表示でも非常にはっきりとしていて見やすいこと、レースペーパーのデザインがかわいらしいこと、背景の色のトーンが落ち着いていること、小さな画像がアクセントとしてうまく使われていることなどから、女性の対象読者にふさわしいデザインと考えました。

■ 提案者全員のお礼・コメント

このたびは素晴らしいデザインをご提案くださり本当にありがとうございました。一人一人にお礼を言うことができなくて申し訳ありません。皆様にはグルテンとは何かというところから調べていただき、時間をかけて対象読者に合った素敵なデザインを考えていただき、本当に感謝しております。どのデザインもそれぞれに特徴があって素晴らしく、1つを選定することは非常に難しい作業でした。全員に金銭的なお礼ができないことを心苦しく思っております。このたびは本当にありがとうございました。今後の皆様のご活躍をお祈りいたします。

```html
<!DOCTYPE html>
<html lang="ja">
<head>
<meta charset="utf-8">
<title>ひだまり食卓ノート</title>
<link href="https://fonts.googleapis.com/css2?family=Shippori+Mincho:wght@400&display=swap" rel="stylesheet">
<style>
  :root {
    --frame-brown: #4b3627;
    --title-green: #2f8a47;
    --band-pink: #e2488f;
    --text-white: #ffffff;
    --photo-dark: #3e2c1f;
    --photo-mid: #8a6446;
    --photo-bread: #d9b48a;
    --photo-crust: #b7875a;
    --photo-wood: #a67a4c;
    --badge-red: #c8373c;
  }
  html, body {
    margin: 0;
    padding: 0;
    overflow: hidden;
    background: #ffffff;
  }
  .cover {
    position: relative;
    width: 849px;
    height: 1200px;
    background: var(--frame-brown);
    overflow: hidden;
    font-family: "Shippori Mincho", serif;
    color: var(--text-white);
  }
  .title-panel {
    position: absolute;
    left: 62px;
    top: 62px;
    width: 725px;
    height: 405px;
    background: var(--title-green);
  }
  .title {
    margin: 0;
    position: absolute;
    left: 62px;
    top: 28px;
    font-weight: 400;
    font-size: 86px;
    line-height: 170px;
    letter-spacing: 4px;
  }
  .title span { display: block; }
  .photo {
    position: absolute;
    left: 62px;
    top: 467px;
    width: 725px;
    height: 467px;
    background:
      radial-gradient(ellipse 150px 80px at 130px 180px, rgba(217,180,138,0.9), rgba(217,180,138,0) 100%),
      radial-gradient(ellipse 150px 80px at 360px 190px, rgba(226,190,148,0.95), rgba(226,190,148,0) 100%),
      radial-gradient(ellipse 150px 80px at 600px 185px, rgba(217,180,138,0.9), rgba(217,180,138,0) 100%),
      radial-gradient(ellipse 90px 50px at 80px 60px, rgba(240,200,140,0.55), rgba(240,200,140,0) 100%),
      radial-gradient(ellipse 120px 60px at 620px 50px, rgba(200,190,170,0.45), rgba(200,190,170,0) 100%),
      linear-gradient(180deg, var(--photo-dark) 0%, var(--photo-mid) 24%, var(--photo-crust) 40%, var(--photo-bread) 52%, var(--photo-wood) 62%, #c89a66 76%, var(--photo-wood) 90%, #6a4a30 100%);
  }
  .info-band {
    position: absolute;
    left: 0;
    top: 934px;
    width: 849px;
    height: 266px;
    background: var(--band-pink);
  }
  .catch-copy {
    position: absolute;
    left: 51px;
    top: 34px;
    margin: 0;
    font-size: 40px;
    line-height: 62px;
    letter-spacing: 1px;
  }
  .catch-copy span { display: block; }
  .author {
    position: absolute;
    left: 51px;
    top: 200px;
    margin: 0;
    font-size: 38px;
    line-height: 46px;
    display: flex;
  }
  .author-label { width: 204px; }
  .author-name { letter-spacing: 7px; }
  .badge {
    position: absolute;
    left: 744px;
    top: 1092px;
  }
</style>
</head>
<body>
  <main class="cover">
    <section class="title-panel">
      <h1 class="title"><span>ひだまり</span><span>食卓ノート</span></h1>
    </section>

    <div class="photo" role="img" aria-label="木箱に並んだグルテンフリーのパン3斤の写真"></div>

    <section class="info-band">
      <p class="catch-copy">
        <span>グルテンフリー食生活で体をいたわり</span>
        <span>真の健康を目指しましょう</span>
      </p>
      <p class="author"><span class="author-label">著者</span><span class="author-name">ロウェンタール・ミサキ</span></p>
    </section>

    <svg class="badge" width="98" height="98" viewBox="0 0 98 98" aria-hidden="true">
      <circle cx="49" cy="49" r="47" fill="#ffffff"/>
      <circle cx="49" cy="49" r="37" fill="var(--badge-red)"/>
    </svg>
  </main>
</body>
</html>
```